Brightloom Reach - Business Card

We need a business card for a Social Media Marketing company that specializes in online marketing for small businesses in Canada using common Social Media platforms such as Instagram, Facebook, Snapchat & Twitter.

I have uploaded a copy of our logo which I would like utilized in the business card. We would like the business card to be modern yet classy design.

Our website is www.brightloomreach.ca

Industry/Entity Type

Marketing

Contact Information for Business Card

Email: info@brightloomreach.ca
Website: www.brightloomreach.ca
Telephone: 604-352-9081

Colors

Designer to choose colors to be used in the design.

Requirements
Must have
• Social Media icons on reverse
• Please add some designs with color.

```html
<!DOCTYPE html>
<html lang="en">
<head>
<meta charset="utf-8">
<title>Brightloom Reach – Business Card</title>
<link rel="stylesheet" href="https://fonts.googleapis.com/css2?family=Oswald:wght@600&family=Montserrat:wght@600&family=Questrial&family=Pinyon+Script&display=swap">
<style>
  :root {
    --backdrop: #33282e;
    --card-dark: #0e0d1c;
    --ink-light: #ffffff;
    --ink-soft: #d9d9e0;
    --photo-warm: #8a6a55;
    --photo-grey: #a9a7a6;
    --photo-deep: #4b3a33;
  }
  * { box-sizing: border-box; margin: 0; padding: 0; }
  html, body {
    width: 1200px; height: 1200px; overflow: hidden;
    background: var(--backdrop);
  }
  .canvas {
    position: relative; width: 1200px; height: 1200px;
  }
  .card {
    position: absolute; left: 270px; width: 660px; height: 372px;
    overflow: hidden;
    box-shadow: 0 14px 30px rgba(0,0,0,0.35);
  }
  .card--front { top: 190px; }
  .card--back { top: 640px; background: var(--card-dark); }

  .card__photo {
    position: absolute; inset: 0;
    background:
      radial-gradient(ellipse at 25% 45%, rgba(196,140,110,0.55), transparent 55%),
      radial-gradient(ellipse at 80% 30%, rgba(220,220,222,0.5), transparent 60%),
      linear-gradient(160deg, var(--photo-grey) 0%, var(--photo-warm) 55%, var(--photo-deep) 100%);
  }
  .card__photo::after {
    content: ""; position: absolute; inset: 0;
    background: rgba(20,18,24,0.28);
  }

  .wordmark {
    position: absolute; display: flex; align-items: center; gap: 14px;
    font-family: "Oswald", sans-serif; font-weight: 600;
    color: var(--ink-light); text-transform: uppercase;
    letter-spacing: 1px; line-height: 0.95;
  }
  .wordmark__mark {
    width: 14px; height: 14px; background: var(--ink-light); flex: none;
  }
  .card--front .wordmark {
    left: 50%; top: 50%; transform: translate(-50%, -50%);
    font-size: 62px; text-align: center;
  }
  .card--back .wordmark {
    left: 390px; top: 140px; font-size: 38px;
  }
  .card--back .wordmark__mark { width: 10px; height: 10px; }

  .person { position: absolute; left: 56px; top: 110px; }
  .person__name {
    font-family: "Pinyon Script", cursive; font-size: 27px;
    color: var(--ink-light); line-height: 1;
  }
  .person__role {
    font-family: "Montserrat", sans-serif; font-weight: 600;
    font-size: 14px; color: var(--ink-light); margin-top: 2px;
  }
  .contacts {
    position: absolute; left: 56px; top: 205px; list-style: none;
    font-family: "Questrial", sans-serif; font-size: 13.5px; color: var(--ink-soft);
  }
  .contacts li { display: flex; align-items: center; gap: 9px; margin-bottom: 16px; }
  .contacts svg { width: 12px; height: 12px; fill: var(--ink-soft); flex: none; }
</style>
</head>
<body>
<main class="canvas">
  <section class="card card--front">
    <div class="card__photo" role="img" aria-label="Photo of a group of friends laughing and sharing pizza while taking a selfie"></div>
    <div class="wordmark"><span>Brightloom<br>Reach</span></div>
  </section>

  <section class="card card--back">
    <div class="person">
      <p class="person__name">Mr. Lorem Ipsum</p>
      <p class="person__role">General Manager</p>
    </div>
    <ul class="contacts">
      <li>
        <svg viewBox="0 0 12 12" aria-hidden="true"><circle cx="6" cy="6" r="5.5"/><path d="M0.5 6h11M6 0.5v11" stroke="#0e0d1c" stroke-width="1"/></svg>
        <span>www.brightloomreach.ca</span>
      </li>
      <li>
        <svg viewBox="0 0 12 12" aria-hidden="true"><path d="M2.4 0.6l2 2.3-1.1 1.5c.7 1.6 2 2.9 3.6 3.6l1.5-1.1 2.3 2-1 2C5 10.7 1.3 7 .5 1.6z"/></svg>
        <span>604-352-9081</span>
      </li>
      <li>
        <svg viewBox="0 0 12 12" aria-hidden="true"><path d="M0.5 2.5h11v7h-11z"/><path d="M0.5 2.5L6 7l5.5-4.5" fill="none" stroke="#0e0d1c" stroke-width="1"/></svg>
        <span>info@brightloomreach.ca</span>
      </li>
    </ul>
    <div class="wordmark"><span class="wordmark__mark"></span><span>Brightloom<br>Reach</span></div>
  </section>
</main>
</body>
</html>
```